Coralview Health Academy Open House

We need to create an advertisement for an upcoming open house that we are conducting. We can create a design in the dimensions of 10" (w) x 13.67" (h). Once that is approved, I will need the ad resized in the following dimensions:

8.5" (w) x 11" (h) - PDF
2400 pixels wide X 2400 pixels height - JPEG

Target Market(s)

Aspiring medical students

Industry/Entity Type

Medical

Requirements
Must have
• Logo
• Tag line: STUDY MEDICINE IN THE CARIBBEAN, BECOME A DOC IN THE US
• One of the attachments has a JPEG file with all the information to include in this new ad however the event location has changed to this:
• Sunday, April 22nd at 1pm at:
• Lantern Lodge Chicago Depot Square
• 718 N. Birch Court
• Chicago, IL 60654
• Event will be held on the 15th floor in The Penwick Room
• FREE parking. Refreshments will be served.
• Change email to admissions@chaheal.org
• Use a nice background and creative design. The details of the event need to be big and emphasize OPEN HOUSE.

```html
<!DOCTYPE html>
<html lang="en">
<head>
<meta charset="utf-8">
<title>Coralview Health Academy Open House</title>
<link rel="stylesheet" href="https://fonts.googleapis.com/css2?family=Oswald:wght@500;700&family=Open+Sans:wght@400;600;700;800&display=swap">
<style>
  :root {
    --navy: #1d3f8f;
    --blue: #2457b8;
    --red: #d2232a;
    --ink: #2a2a2a;
    --paper: #ffffff;
    --mist: #eef0f4;
    --photo-a: #b9cde6;
    --photo-b: #e9eef5;
  }
  * { box-sizing: border-box; margin: 0; padding: 0; }
  html, body { width: 900px; height: 1200px; overflow: hidden; background: #d9d9d9; }
  .flyer {
    position: relative; width: 900px; height: 1200px; overflow: hidden;
    background: linear-gradient(160deg, var(--paper) 55%, var(--mist) 55%);
    font-family: "Open Sans", Arial, sans-serif; color: var(--ink);
  }
  .hero-photo {
    position: absolute; top: 0; right: 0; width: 620px; height: 330px;
    background: linear-gradient(120deg, var(--photo-b), var(--photo-a));
  }
  .brand {
    position: absolute; top: 50px; left: 40px; width: 250px;
    display: flex; flex-direction: column; align-items: center; gap: 12px;
  }
  .brand-dot { width: 150px; height: 150px; border-radius: 50%; background: var(--navy); }
  .brand-name { font-weight: 700; font-size: 20px; color: var(--navy); text-align: center; line-height: 1.2; }
  .event-bar { position: absolute; top: 300px; left: 0; width: 900px; height: 70px; }
  .open-house {
    position: absolute; left: 0; top: 0; width: 440px; height: 70px; background: var(--navy);
    color: #fff; font-family: "Oswald", sans-serif; font-weight: 700; font-size: 46px;
    padding-left: 40px; line-height: 70px;
  }
  .date {
    position: absolute; right: 0; top: 0; width: 470px; height: 70px; background: var(--red);
    color: #fff; font-family: "Oswald", sans-serif; font-weight: 500; font-size: 30px;
    text-align: right; padding-right: 40px; line-height: 1.05; padding-top: 4px;
  }
  .tagline-band {
    position: absolute; top: 370px; left: 0; width: 900px; height: 120px; background: var(--red);
    color: #fff; text-align: center; font-family: "Oswald", sans-serif; font-weight: 700;
    padding-top: 10px;
  }
  .tagline-band .line1 { font-size: 46px; line-height: 1.15; }
  .tagline-band .line2 { font-size: 38px; line-height: 1.15; font-weight: 500; }
  .band-wedge { position: absolute; top: 490px; left: 0; }
  .highlights { position: absolute; top: 585px; left: 50px; width: 560px; list-style: none; }
  .highlights li {
    font-size: 19px; font-weight: 600; color: var(--ink); margin-bottom: 18px;
    display: flex; align-items: center; gap: 12px; white-space: nowrap;
  }
  .highlights li::before { content: ""; width: 11px; height: 11px; background: var(--red); flex: none; }
  .perks {
    position: absolute; top: 585px; right: 40px; width: 210px; height: 210px; border-radius: 50%;
    background: var(--blue); border: 4px dotted #fff; outline: 6px solid var(--blue);
    color: #fff; display: flex; flex-direction: column; align-items: center; justify-content: center;
    text-align: center; gap: 10px; font-size: 19px; line-height: 1.2;
  }
  .perks hr { width: 60%; border: none; border-top: 2px dashed #fff; }
  .venue-label {
    position: absolute; top: 850px; left: 360px; width: 180px; height: 46px; background: var(--red);
    color: #fff; font-family: "Oswald", sans-serif; font-size: 28px; text-align: center; line-height: 46px;
  }
  .venue-box {
    position: absolute; top: 872px; left: 120px; width: 660px; height: 165px;
    border: 2px solid var(--navy); background: var(--paper); padding: 38px 30px 0;
    font-size: 19px; line-height: 1.5;
  }
  .venue-box p { display: flex; gap: 12px; align-items: flex-start; }
  .venue-box .hotel { padding-left: 28px; }
  .venue-box svg { flex: none; margin-top: 6px; }
  .coupon {
    position: absolute; top: 1058px; left: 40px; width: 820px; height: 50px; border: 2px dashed var(--navy);
    border-radius: 25px; background: var(--paper); text-align: center; line-height: 46px;
    font-weight: 800; font-size: 19px; color: var(--navy);
  }
  .coupon .code { color: var(--red); }
  .footer {
    position: absolute; bottom: 0; left: 0; width: 900px; height: 70px; background: var(--navy);
    color: #fff; display: flex; justify-content: space-around; align-items: center; font-size: 18px;
  }
  .footer span { display: flex; gap: 8px; align-items: center; }
</style>
</head>
<body>
<main class="flyer">
  <div class="hero-photo" role="img" aria-label="Group of smiling medical students in scrubs and white coats"></div>

  <div class="brand">
    <div class="brand-dot"></div>
    <div class="brand-name">Coralview Health Academy</div>
  </div>

  <div class="event-bar">
    <div class="open-house">OPEN HOUSE</div>
    <div class="date">APRIL 22ND ,SUNDAY<br>AT 1PM</div>
  </div>

  <div class="tagline-band">
    <div class="line1">STUDY MEDICINE IN THE CARIBBEAN,</div>
    <div class="line2">BECOME A DOC IN THE US</div>
  </div>
  <svg class="band-wedge" width="900" height="50" viewBox="0 0 900 50">
    <polygon points="0,0 900,0 0,50" fill="var(--navy)"/>
  </svg>

  <ul class="highlights">
    <li>4 year md program</li>
    <li>Financial aid | student dorms</li>
    <li>Modern campus | Friendly tuition ($5900/semester)</li>
    <li>U.S clinical rotations | 88.9% usmle passing rate</li>
    <li>Canadian loans Available</li>
  </ul>

  <div class="perks">
    <div><strong>FREE</strong> parking</div>
    <hr>
    <div>Refreshments will<br>be served.</div>
  </div>

  <div class="venue-box">
    <p>
      <svg width="16" height="16" viewBox="0 0 16 16"><rect width="16" height="16" fill="var(--red)"/></svg>
      <span>Event will be held on the 15th floor in The Penwick Room</span>
    </p>
    <p class="hotel">Lantern Lodge Chicago Depot Square</p>
    <p>
      <svg width="16" height="20" viewBox="0 0 16 20"><path d="M8 0a7 7 0 0 0-7 7c0 5 7 13 7 13s7-8 7-13a7 7 0 0 0-7-7zm0 10a3 3 0 1 1 0-6 3 3 0 0 1 0 6z" fill="var(--red)"/></svg>
      <span>718 N. Birch Court | Chicago, IL 60654</span>
    </p>
  </div>
  <div class="venue-label">Venue</div>

  <div class="coupon">HAVE YOUR ENTIRE APPLICATION FEE WAIVED. ENTER COUPON CODE: <span class="code">OPHUS</span></div>

  <footer class="footer">
    <span>
      <svg width="18" height="18" viewBox="0 0 24 24"><path d="M6.6 10.8a15 15 0 0 0 6.6 6.6l2.2-2.2a1 1 0 0 1 1-.25 11.4 11.4 0 0 0 3.6.57 1 1 0 0 1 1 1V20a1 1 0 0 1-1 1A17 17 0 0 1 3 4a1 1 0 0 1 1-1h3.5a1 1 0 0 1 1 1c0 1.25.2 2.45.57 3.57a1 1 0 0 1-.25 1z" fill="#fff"/></svg>
      555-014-2290
    </span>
    <span>
      <svg width="20" height="14" viewBox="0 0 20 14"><rect x="1" y="1" width="18" height="12" fill="none" stroke="#fff" stroke-width="2"/><path d="M1 1l9 7 9-7" fill="none" stroke="#fff" stroke-width="2"/></svg>
      admissions@chaheal.org
    </span>
    <span>
      <svg width="18" height="18" viewBox="0 0 18 18"><circle cx="9" cy="9" r="8" fill="none" stroke="#fff" stroke-width="2"/><path d="M1 9h16M9 1c3 3 3 13 0 16M9 1c-3 3-3 13 0 16" fill="none" stroke="#fff" stroke-width="1.5"/></svg>
      CHAHEAL.org
    </span>
  </footer>
</main>
</body>
</html>
```